Business card design for web travel company

Hi
we'd like to receive some proposal for a business card design.
Stayvano is a private travel club, dedicated to all travel lovers, with unique offers for exclusive destinations all around the world. At Stayvano you can find a wide range of offers for resorts, boutique hotels and travel packages at the best guaranteed price available on the market. The convenience of the offer is guaranteed by a private sales model: offers are available for a limited time only and they are personally chosen by Stayvano's qualified team of travel experts.
We offer only exclusive hotels with discounted prices but we are not an outlet or a discount supermarket: the design should reflect our connection with luxury, exclusivity using the same style of our website www.stayvano-example.com.
We want to make sure that when we'll present ourself to our business partner they will feel immediately which is our brand positioning giving them also a sense of an affordable and reliable partner.
In attachment you can also find our brand guidelines (please note that we are NOT USING ANY MORE THE TAG LINE "Five star outlet" mentioned in it).
The info to be inserted are:
Name Surname
Job Title
Tel
Mobile (when needed)
Email
Stayvano S.r.l.
Via Bruno Lesta 27
20131 Milano

```html
<!DOCTYPE html>
<html lang="it">
<head>
<meta charset="utf-8">
<title>Stayvano – Business Card</title>
<link href="https://fonts.googleapis.com/css2?family=Arimo:ital,wght@0,400;0,700;1,700&display=swap" rel="stylesheet">
<style>
  :root {
    --page-bg: #e8e8e8;
    --card-dark: #383838;
    --card-dark-edge: #2f2f2f;
    --card-light: #ffffff;
    --ink: #1a1a1a;
    --ink-muted: #4a4a4a;
    --logo-white: #ffffff;
    --url-bar: #111111;
  }
  * { box-sizing: border-box; margin: 0; padding: 0; }
  html, body {
    width: 1200px; height: 900px; overflow: hidden;
    background: var(--page-bg);
    font-family: "Arimo", Arial, sans-serif;
  }
  .stage { position: relative; width: 1200px; height: 900px; }

  .card {
    position: absolute; top: 310px; height: 280px; overflow: hidden;
  }
  .card--front { left: 54px; width: 506px; }
  .card--back  { left: 646px; width: 504px; background: var(--card-light); }

  .texture {
    position: absolute; inset: 0;
    background: linear-gradient(160deg, var(--card-dark) 0%, var(--card-dark-edge) 100%);
  }

  .front-logo {
    position: absolute; left: 0; right: 0; top: 82px;
    text-align: center; color: var(--logo-white);
    font-size: 62px; line-height: 72px; font-weight: 400; letter-spacing: 1px;
    white-space: nowrap;
  }
  .url-bar {
    position: absolute; left: 98px; width: 310px; top: 226px; height: 34px;
    background: var(--url-bar); color: var(--logo-white);
    font-size: 18px; line-height: 34px; text-align: center;
    white-space: nowrap;
  }

  .back-info {
    position: absolute; inset: 0; color: var(--ink);
    font-size: 17px; line-height: 23px; white-space: nowrap;
  }
  .identity { position: absolute; right: 322px; top: 40px; text-align: right; }
  .identity .name { font-weight: 700; }
  .identity .role { font-weight: 700; font-style: italic; color: var(--ink-muted); margin-top: 6px; }
  .company { position: absolute; left: 196px; top: 40px; }
  .company .firm { font-weight: 700; }
  .contacts { position: absolute; left: 196px; top: 124px; list-style: none; }
  .contacts li { display: flex; }
  .contacts .label { width: 20px; font-weight: 700; }

  .back-band { position: absolute; left: 0; right: 0; bottom: 0; height: 66px; }
  .back-logo {
    position: absolute; left: 20px; top: 14px;
    color: var(--logo-white); font-size: 32px; line-height: 38px; font-weight: 400;
  }
</style>
</head>
<body>
<main class="stage">
  <section class="card card--front">
    <div class="texture" role="img" aria-label="Dark charcoal diagonal pinstripe texture"></div>
    <div class="front-logo">Stayvano</div>
    <div class="url-bar">www.stayvano-example.com</div>
  </section>

  <section class="card card--back">
    <div class="back-info">
      <div class="identity">
        <p class="name">Luca Ferri</p>
        <p class="role">MANAGER</p>
      </div>
      <div class="company">
        <p class="firm">Stayvano S.r.l.</p>
        <p>Via Bruno Lesta 27</p>
        <p>20131 Milano</p>
      </div>
      <ul class="contacts">
        <li><span class="label">T</span><span>06911238840</span></li>
        <li><span class="label">M</span><span>01211457720</span></li>
        <li><span class="label">E</span><span>LucaFerri@stayvano-example.com</span></li>
      </ul>
    </div>
    <div class="back-band">
      <div class="texture" role="img" aria-label="Dark charcoal diagonal pinstripe texture"></div>
      <div class="back-logo">Stayvano</div>
    </div>
  </section>
</main>
</body>
</html>
```